Plakat-Design für einen Pflegedienst
Zielgruppe
Unter Pflegedienst besteht jetzt seit 10 Jahren, Dazu würden wir gerne ein Werbeplakat an verschiedenen Standpunkten veröffentlichen. Draus sollte hervorgehen, dass wir 10 Jahre bestehen Bilder sollten aus den Portalen verwendet werden. Der Slogan könnte vielleicht lauten:
Seit 10 Jahren rund um die Uhr für Sie im Einsatz.
oder gerne auch eine andere Idee für den Slogan.
Die Plakate sollen bei 468 Aushang veröffentlicht werden. Da wir zwei Filialen betrieben, müssten zwei verschiedene Varianten mit zwei Logos und Telefonnummern erstellt werden.
Aufgabenstellung
Das Plakat sollte modern und elegant sein.

```html
<!DOCTYPE html>
<html lang="de">
<head>
<meta charset="utf-8">
<title>Pflegedienst Tulpexor – Plakat</title>
<link rel="stylesheet" href="https://fonts.googleapis.com/css2?family=Quicksand:wght@600;700&family=Josefin+Sans:wght@700&display=swap">
<style>
  :root {
    --page-bg: #ffffff;
    --teal: #1ea9b9;
    --teal-light: #52c0cc;
    --band-yellow: #ebc94f;
    --band-orange: #f5aa1c;
    --accent-yellow: #e6bf2e;
    --headline-cream: #fdf1d8;
    --white: #ffffff;
    --ink: #111111;
    --photo-wall: #eceeed;
    --photo-room: #e4e2d6;
    --photo-sofa: #ece57a;
    --badge-orange: #f2a43a;
  }
  html, body {
    margin: 0;
    width: 1200px;
    height: 800px;
    overflow: hidden;
    background: var(--page-bg);
  }
  .canvas {
    position: relative;
    width: 1200px;
    height: 800px;
  }
  .poster {
    position: absolute;
    left: 332px;
    top: 20px;
    width: 536px;
    height: 760px;
    display: block;
  }
  .brand-line {
    font-family: "Quicksand", sans-serif;
    font-weight: 700;
    font-size: 38px;
    fill: var(--headline-cream);
  }
  .headline {
    font-family: "Quicksand", sans-serif;
    font-weight: 700;
    font-size: 72px;
    fill: var(--white);
  }
  .subline {
    font-family: "Quicksand", sans-serif;
    font-weight: 700;
    font-size: 68px;
    fill: var(--white);
  }
  .anniversary {
    font-family: "Josefin Sans", sans-serif;
    font-weight: 700;
    font-size: 36px;
    fill: var(--white);
  }
  .logo-placeholder {
    font-family: "Josefin Sans", sans-serif;
    font-weight: 700;
    font-size: 34px;
    fill: var(--ink);
    letter-spacing: 3px;
  }
  .contact {
    font-family: "Josefin Sans", sans-serif;
    font-weight: 700;
    font-size: 16px;
    fill: var(--white);
    letter-spacing: 3px;
  }
</style>
</head>
<body>
<main class="canvas">
  <svg class="poster" viewBox="0 0 797 1130" xmlns="http://www.w3.org/2000/svg" aria-label="Plakat Pflegedienst Tulpexor">
    <defs>
      <linearGradient id="poster-bg" x1="0" y1="1" x2="1" y2="0">
        <stop offset="0.45" stop-color="var(--teal)"/>
        <stop offset="1" stop-color="var(--teal-light)"/>
      </linearGradient>
      <linearGradient id="photo-tones" x1="0" y1="0" x2="0" y2="1">
        <stop offset="0" stop-color="var(--photo-wall)"/>
        <stop offset="0.42" stop-color="var(--photo-room)"/>
        <stop offset="0.62" stop-color="var(--photo-sofa)"/>
        <stop offset="1" stop-color="#d9d7c0"/>
      </linearGradient>
    </defs>

    <rect class="poster-background" width="797" height="1130" fill="url(#poster-bg)"/>

    <polygon class="band band-top" points="50,86 670,18 676,80 56,146" fill="var(--band-orange)"/>
    <text class="brand-line" x="72" y="124" textLength="578" lengthAdjust="spacingAndGlyphs"
          transform="rotate(-5.6 72 124)">PFLEGEDIENST TULPEXOR</text>

    <polygon class="band band-headline" points="0,152 752,78 765,206 0,280" fill="var(--band-yellow)"/>
    <text class="headline" x="40" y="238" textLength="682" lengthAdjust="spacingAndGlyphs"
          transform="rotate(-5.6 40 238)">RUND UM DIE UHR</text>

    <circle class="photo-accent" cx="412" cy="562" r="304" fill="var(--accent-yellow)"/>
    <circle class="photo" cx="397" cy="556" r="302" fill="url(#photo-tones)" role="img"
            aria-label="Foto: Pflegerin im Gespräch mit einer älteren Dame im Rollstuhl vor einem gelben Sofa"/>

    <circle class="service-badge" cx="160" cy="405" r="68" fill="var(--badge-orange)" role="img"
            aria-label="Rosette mit Hinweis auf Erreichbarkeit rund um die Uhr"/>

    <polygon class="band band-subline" points="77,878 797,808 797,936 85,992" fill="var(--band-yellow)"/>
    <text class="subline" x="136" y="960" textLength="620" lengthAdjust="spacingAndGlyphs"
          transform="rotate(-5 136 960)">für Sie im Einsatz</text>

    <polygon class="band band-anniversary" points="86,996 797,930 797,1010 96,1080" fill="var(--band-orange)"/>
    <text class="anniversary" x="356" y="1030" textLength="372" lengthAdjust="spacingAndGlyphs"
          transform="rotate(-5 356 1030)">SEIT 10 JAHREN</text>

    <polygon class="logo-box" points="88,986 236,973 242,1068 94,1080" fill="var(--white)"/>
    <text class="logo-placeholder" x="130" y="1018" transform="rotate(-4 130 1018)">IHR</text>
    <text class="logo-placeholder" x="110" y="1062" transform="rotate(-4 110 1062)">LOGO</text>

    <g class="contact" transform="rotate(-3 750 1080)">
      <text x="748" y="1062" text-anchor="end">KONTAKT</text>
      <text x="750" y="1084" text-anchor="end">STRASSE</text>
      <text x="752" y="1106" text-anchor="end">PLZ ORT</text>
    </g>
  </svg>
</main>
</body>
</html>
```